New Business Card & Logo Design Project for PR Agency

Halvery & Associates Tech Public Relations agency is looking for a new business card design. Please see our website at www.halvery-pr.example for a description of our services. The design does not necessarily have to match the website’s aesthetic as we are looking for something fresh and modern that reflects our business. We want to emphasize that our focus is on media & public relations, content creation, social media and SEO. We want the business card to convey our BtoB technology focus and should have a very clean look. You are welcome to draw from our current halvery & associates logo on the card or play with that design too. We also like the idea of utilizing blue and white, which are often used in technology-related designs and layouts.
Attached are jpegs of the current logo and current card design for your reference.
Target Market(s)
Our clients are Business-to-Business technology providers.We sell our services to the CEO/President/Marketing director of a technology providing company.
Industry/Entity Type
Business
Look and feel

```html
<!DOCTYPE html>
<html lang="en">
<head>
<meta charset="utf-8">
<title>Halvery &amp; Associates — Business Card</title>
<link rel="stylesheet" href="https://fonts.googleapis.com/css2?family=Open+Sans:wght@400;700&family=Tinos:wght@400;700&display=swap">
<style>
  :root {
    --page-bg: #e9e6e2;
    --card-bg: #ffffff;
    --card-edge: #d4d0cb;
    --ink: #111111;
    --ink-soft: #444444;
    --ink-muted: #555555;
    --accent-red: #d8262f;
    --band-blue: #26a6dc;
    --rule: #111111;
    --divider: #c9c9c9;
  }
  * { box-sizing: border-box; margin: 0; padding: 0; }
  html, body { width: 1200px; height: 1168px; overflow: hidden; }
  body { background: var(--page-bg); position: relative; font-family: "Open Sans", Arial, sans-serif; }

  .card {
    position: absolute;
    width: 937px;
    height: 538px;
    background: var(--card-bg);
    border: 1px solid var(--card-edge);
    border-radius: 0 48px 0 48px;
    overflow: hidden;
  }
  .card--front { left: 44px; top: 29px; }
  .card--back { left: 218px; top: 588px; }

  .wordmark {
    position: absolute;
    left: 0; right: 0;
    text-align: center;
    font-family: "Open Sans", Arial, sans-serif;
    font-weight: 700;
    font-size: 50px;
    color: var(--ink);
    letter-spacing: 0.5px;
    line-height: 1;
  }
  .card--front .wordmark { top: 98px; }
  .card--back .wordmark { top: 238px; }

  .tagline-band {
    position: absolute;
    left: 0; right: 0;
    top: 242px;
    height: 66px;
    border-top: 4px solid var(--rule);
    border-bottom: 4px solid var(--rule);
  }
  .tagline-band__fill {
    position: absolute;
    left: 0; right: 0;
    top: 3px; bottom: 3px;
    background: var(--band-blue);
    color: #fff;
    font-family: "Tinos", "Times New Roman", serif;
    font-size: 29px;
    display: flex;
    align-items: center;
    justify-content: center;
  }

  .holder {
    position: absolute;
    right: calc(937px - 449px);
    top: 336px;
    text-align: right;
  }
  .holder__name { font-size: 28px; font-weight: 700; color: var(--ink-soft); line-height: 34px; }
  .holder__title { font-size: 22px; color: var(--accent-red); line-height: 28px; }
  .holder__address { margin-top: 20px; font-size: 22px; color: var(--ink-muted); line-height: 32px; }

  .column-divider {
    position: absolute;
    left: 474px; top: 340px;
    width: 1px; height: 162px;
    background: var(--divider);
  }

  .contact-list {
    position: absolute;
    left: 496px; top: 346px;
    list-style: none;
  }
  .contact-list li {
    display: flex;
    align-items: center;
    height: 40px;
    font-size: 23px;
    color: var(--ink-soft);
  }
  .contact-list svg { width: 20px; height: 20px; margin-right: 12px; flex: none; }

  .back-tagline {
    position: absolute;
    left: 0; right: 0; top: 326px;
    text-align: center;
    font-family: "Tinos", "Times New Roman", serif;
    font-weight: 700;
    font-size: 28px;
    letter-spacing: 2px;
    color: var(--ink-soft);
  }
  .back-web {
    position: absolute;
    left: 0; right: 0; top: 469px;
    text-align: center;
    font-size: 23px;
    letter-spacing: 5px;
    color: var(--ink-soft);
  }
</style>
</head>
<body>

<section class="card card--front">
  <div class="wordmark">halvery &amp; associates</div>

  <div class="tagline-band">
    <div class="tagline-band__fill">A public Relation Company</div>
  </div>

  <div class="holder">
    <div class="holder__name">Daniel Ortwin</div>
    <div class="holder__title">Partner</div>
    <div class="holder__address">48 Linden Avenue, Suite 2<br>Fairhaven, Vermont 05099</div>
  </div>

  <div class="column-divider"></div>

  <ul class="contact-list">
    <li>
      <svg viewBox="0 0 20 20" aria-hidden="true"><circle cx="10" cy="10" r="8.5" fill="none" stroke="var(--accent-red)" stroke-width="1.6"/><path d="M7 5.5c-1 1-1 3 .8 5.6s4 3.7 5.2 3.2l.9-1.4-2-1.4-1 .8c-.8-.3-2-1.6-2.4-2.5l.8-1-1.3-2.1z" fill="var(--accent-red)"/></svg>
      (555) 014-7720
    </li>
    <li>
      <svg viewBox="0 0 20 20" aria-hidden="true"><rect x="5" y="3" width="10" height="5" fill="var(--accent-red)"/><rect x="1.5" y="8" width="17" height="7" rx="1.5" fill="var(--accent-red)"/><rect x="5" y="13" width="10" height="4" fill="#fff" stroke="var(--accent-red)" stroke-width="1.4"/></svg>
      (555) 014-7720
    </li>
    <li>
      <svg viewBox="0 0 20 20" aria-hidden="true"><rect x="2" y="5" width="16" height="11" rx="1" fill="var(--accent-red)"/><path d="M2.5 5.8 10 11l7.5-5.2" fill="none" stroke="#fff" stroke-width="1.5"/></svg>
      dortwin@halvery-pr.example
    </li>
    <li>
      <svg viewBox="0 0 20 20" aria-hidden="true"><g fill="none" stroke="var(--accent-red)" stroke-width="1.4"><circle cx="10" cy="10" r="7.5"/><ellipse cx="10" cy="10" rx="3.3" ry="7.5"/><path d="M2.5 10h15M4 6h12M4 14h12"/></g></svg>
      www.halvery-pr.example
    </li>
  </ul>
</section>

<section class="card card--back">
  <div class="wordmark">halvery &amp; associates</div>
  <div class="back-tagline">A Public Relation Company</div>
  <div class="back-web">www.halvery-pr.example</div>
</section>

</body>
</html>
```